Oakmere Kin Clinic

We are a doctors surgery, providing medical services to all ages

we aim for a professional as well as an eye catching look for the signs that can be seen by passing vehicles and people who walk by

trustworthy quality medical care to to all patients, we treat like family

Name- Brenwick Kin Clinic Medical practice

Target Market(s)

all ages, adults
the elderly

Industry/Entity Type

Medical

Requirements
Must have
• eye catching,
obvious medical service location

```html
<!DOCTYPE html>
<html lang="en">
<head>
<meta charset="utf-8">
<title>Brenwick Kin Clinic – Street Banner</title>
<link rel="stylesheet" href="https://fonts.googleapis.com/css2?family=Archivo+Black&family=Poppins:wght@600;700&display=swap">
<style>
  :root {
    --page-bg: #ffffff;
    --sky-top: #2eafe9;
    --sky-mid: #7fcdf1;
    --sky-bottom: #d8eefa;
    --navy: #0a5ba6;
    --navy-dark: #06488a;
    --band-edge: #3d8fd6;
    --white: #ffffff;
    --glow: #9fd8f5;
    --photo-light: #eef4f8;
    --photo-mid: #c9dde9;
    --photo-warm: #d9c3b4;
  }
  * { margin: 0; padding: 0; box-sizing: border-box; }
  html, body {
    width: 1200px; height: 654px; overflow: hidden;
    background: var(--page-bg);
  }
  .canvas { position: relative; width: 1200px; height: 654px; }

  .banner {
    position: absolute; left: 69px; top: 185px;
    width: 1064px; height: 283px;
    background: linear-gradient(180deg, var(--sky-top) 0%, var(--sky-mid) 45%, var(--sky-bottom) 100%);
    box-shadow: 4px 5px 6px rgba(0,0,0,0.35);
    overflow: hidden;
  }

  .brand-badge {
    position: absolute; left: 27px; top: 35px;
    width: 146px; height: 146px; border-radius: 50%;
    background: var(--white);
    box-shadow: 0 0 16px 6px rgba(255,255,255,0.85);
    display: flex; align-items: center; justify-content: center;
    text-align: center;
  }
  .brand-name {
    font-family: "Poppins", sans-serif; font-weight: 700;
    font-size: 19px; line-height: 1.15; color: var(--navy);
    width: 110px;
  }

  .headline {
    position: absolute; left: 195px; width: 540px; top: 28px;
    text-align: center;
    font-family: "Archivo Black", sans-serif;
    font-size: 50px; line-height: 55px;
    color: var(--navy);
    -webkit-text-stroke: 6px var(--white);
    paint-order: stroke fill;
    letter-spacing: -0.5px;
    filter: drop-shadow(1px 2px 2px rgba(0,40,90,0.35));
  }
  .tagline {
    position: absolute; left: 195px; width: 540px; top: 167px;
    text-align: center;
    font-family: "Poppins", sans-serif; font-weight: 600;
    font-size: 40px; line-height: 44px;
    color: var(--white);
    -webkit-text-stroke: 6px var(--glow);
    paint-order: stroke fill;
  }

  .photo {
    position: absolute; right: 0; top: 0;
    width: 344px; height: 235px;
    background:
      radial-gradient(ellipse at 35% 55%, var(--photo-warm) 0%, transparent 45%),
      linear-gradient(90deg, rgba(216,238,250,0) 0%, var(--photo-mid) 18%, var(--photo-light) 60%, var(--photo-mid) 100%);
  }

  .promise-band {
    position: absolute; left: 0; bottom: 0;
    width: 100%; height: 48px;
    background: linear-gradient(180deg, var(--navy) 0%, var(--navy-dark) 100%);
    border-top: 3px solid var(--band-edge);
    display: flex; align-items: center; justify-content: center;
  }
  .promise {
    font-family: "Poppins", sans-serif; font-weight: 600;
    font-size: 23px; letter-spacing: 1.6px;
    color: var(--white);
    margin-right: 130px;
  }
</style>
</head>
<body>
  <main class="canvas">
    <section class="banner">
      <div class="brand-badge">
        <span class="brand-name">Oakmere Kin Clinic</span>
      </div>

      <h1 class="headline">Brenwick Kin Clinic<br>Medical practice</h1>
      <p class="tagline">we treat like family</p>

      <div class="photo" role="img" aria-label="Photo of a doctor examining a smiling young boy with a stethoscope"></div>

      <div class="promise-band">
        <p class="promise">Trustworthy quality medical care to all patients</p>
      </div>
    </section>
  </main>
</body>
</html>
```